1/2 page ad, 1/2 HORIZONTAL 9.875" x 5", for magazine

We need an ad design that tastefully describes the services we offer.

The Linden Heritage Centre is the heart of Vancouver. We provide classic, updated banquet halls with integrated audio visual capabilities and soaring ceilings. With nine rental halls we are home for international conferences, intimate family gatherings and celebrations for up to 1400 people. Our central location, free parking and full service catering are an ideal solution for weddings, celebrations of life and Christmas parties. With break out rooms and separate rooms for dining and meeting, we are a tremendous asset for the Vancouver destination conferences, awards nights and ceremonies.

1. A PDF x/1a file (CMYK, all fonts embedded, images 200ppi) Black or grey recommended
% of black only.
2. An Illustrator CS6 (or lower) file or eps file with all fonts converted to outlines and all
images embedded. Colour space must be CMYK, not RGB. Images should be 200ppi

```html
<!DOCTYPE html>
<html lang="en">
<head>
<meta charset="utf-8">
<title>Linden Heritage Centre – Half Page Ad</title>
<link rel="stylesheet" href="https://fonts.googleapis.com/css2?family=Montserrat:wght@400;500;600;700;800&display=swap">
<style>
  :root {
    --red: #e41e26;
    --navy: #26307a;
    --white: #ffffff;
    --ink: #1f1f1f;
    --stage: #d3d1d3;
    --badge-ring: #b9b9bf;
  }
  * { box-sizing: border-box; margin: 0; padding: 0; }
  html, body {
    width: 1200px; height: 695px; overflow: hidden;
    background: var(--stage);
    font-family: "Montserrat", sans-serif;
  }
  .ad {
    position: absolute; left: 83px; top: 84px;
    width: 1033px; height: 522px;
    background: linear-gradient(180deg, #ffffff 0%, #f4f4f5 60%, #ffffff 100%);
    overflow: hidden;
  }
  .ad-shapes { position: absolute; inset: 0; width: 100%; height: 100%; }

  .headline {
    position: absolute; left: 32px; top: 27px;
    font-weight: 800; font-size: 36px; line-height: 34px;
    color: var(--navy); letter-spacing: 0.2px;
  }
  .headline .accent { color: var(--red); }
  .headline-rule {
    position: absolute; left: 32px; top: 174px;
    width: 43px; height: 3px; background: var(--navy);
  }
  .intro {
    position: absolute; left: 32px; top: 191px; width: 440px;
    font-weight: 500; font-size: 14px; line-height: 20.4px; color: var(--ink);
  }
  .services-label {
    position: absolute; left: 29px; top: 270px;
    width: 173px; height: 33px; background: var(--red);
    color: var(--white); font-weight: 800; font-size: 18.5px;
    display: flex; align-items: center; justify-content: center;
  }
  .services {
    position: absolute; left: 29px; top: 312px;
    display: grid; grid-template-columns: 188px 200px;
    list-style: none; row-gap: 0;
  }
  .services li {
    display: flex; align-items: center; gap: 4px;
    font-size: 23.5px; line-height: 23px; color: var(--ink); font-weight: 400;
    height: 23px;
  }
  .services svg { width: 19px; height: 19px; flex: none; }

  .call { position: absolute; left: 28px; top: 429px; color: var(--white); }
  .call-title { font-weight: 700; font-size: 16.5px; line-height: 18px; }
  .call-sub { font-weight: 500; font-size: 15px; line-height: 18px; }
  .phone {
    position: absolute; left: 29px; top: 467px; width: 247px; height: 35px;
    background: var(--red); color: var(--white);
    display: flex; align-items: center; gap: 8px; padding-left: 6px;
    font-weight: 700; font-size: 26px;
  }
  .phone svg { width: 28px; height: 28px; flex: none; }
  .footer-divider {
    position: absolute; left: 283px; top: 426px; width: 1px; height: 76px;
    background: rgba(255,255,255,0.7);
  }
  .contact {
    position: absolute; left: 299px; top: 424px; list-style: none; color: var(--white);
  }
  .contact li { display: flex; align-items: flex-start; gap: 7px; }
  .contact svg { width: 18px; height: 18px; flex: none; margin-top: 1px; }
  .contact .address { font-weight: 700; font-size: 14.5px; line-height: 17px; margin-bottom: 6px; }
  .contact .line { font-weight: 500; font-size: 15px; line-height: 18px; margin-bottom: 4px; align-items: center; }
  .contact .line svg { margin-top: 0; }

  .badge {
    position: absolute; left: 784px; top: 428px; width: 174px; height: 174px;
    margin-top: -87px;
    border-radius: 50%; background: var(--white);
    border: 3px solid var(--badge-ring);
    display: flex; align-items: center; justify-content: center; text-align: center;
    color: var(--navy); font-weight: 800; font-size: 17px; line-height: 20px;
  }
</style>
</head>
<body>
  <div class="ad">
    <svg class="ad-shapes" viewBox="0 0 1721 870" preserveAspectRatio="none" aria-hidden="true">
      <defs>
        <linearGradient id="hallTones" x1="0" y1="0" x2="0" y2="1">
          <stop offset="0" stop-color="#f2f0ec"/>
          <stop offset="0.3" stop-color="#e6ded2"/>
          <stop offset="0.52" stop-color="#e8d6b8"/>
          <stop offset="0.66" stop-color="#d8b592"/>
          <stop offset="1" stop-color="#c7744a"/>
        </linearGradient>
      </defs>
      <path d="M0 662 C 300 692 620 680 860 612 L 1000 590 L 1000 870 L 0 870 Z" fill="var(--navy)"/>
      <path d="M906 0 C 820 200 815 470 870 620 C 900 720 920 800 940 870 L1721 870 L1721 0 Z" fill="var(--red)"/>
      <path d="M963 0 C 890 200 885 440 925 580 C 955 700 1010 800 1070 870 L1721 870 L1721 0 Z" fill="var(--navy)"/>
      <path d="M1021 0 C 945 200 935 430 972 570 C 1000 690 1060 800 1110 870 L1721 870 L1721 0 Z" fill="var(--red)"/>
    </svg>
    <svg class="ad-shapes" viewBox="0 0 1721 870" preserveAspectRatio="none" role="img" aria-label="Photo of the banquet hall set for a wedding: round tables with white linens, gold chairs, flower centrepieces, draped stage and wooden dance floor">
      <path d="M1121 0 C 990 120 910 380 945 560 C 975 700 1050 800 1131 870 L1721 870 L1721 0 Z" fill="url(#hallTones)" stroke="var(--white)" stroke-width="5"/>
    </svg>

    <h1 class="headline"><span class="accent">PERFECT VENUE</span><br>FOR ANY SIZE OR<br>TYPE OF EVENT YOU<br>ARE LOOKING TO HOST.</h1>
    <div class="headline-rule"></div>
    <p class="intro">The Linden Heritage Centre celebrated it’s grand opening in 1986 and has since then become a well respected multipurpose facility in the city of Vancouver.</p>

    <div class="services-label">OUR SERVICES</div>
    <ul class="services">
      <li><svg viewBox="0 0 20 20"><circle cx="9" cy="11" r="7.5" fill="none" stroke="var(--red)" stroke-width="1.8"/><path d="M5 10.5 L9 14.5 L18 3" fill="none" stroke="var(--red)" stroke-width="2.2" stroke-linecap="round" stroke-linejoin="round"/></svg>WEDDINGS</li>
      <li><svg viewBox="0 0 20 20"><circle cx="9" cy="11" r="7.5" fill="none" stroke="var(--red)" stroke-width="1.8"/><path d="M5 10.5 L9 14.5 L18 3" fill="none" stroke="var(--red)" stroke-width="2.2" stroke-linecap="round" stroke-linejoin="round"/></svg>BAR SERVICES</li>
      <li><svg viewBox="0 0 20 20"><circle cx="9" cy="11" r="7.5" fill="none" stroke="var(--red)" stroke-width="1.8"/><path d="M5 10.5 L9 14.5 L18 3" fill="none" stroke="var(--red)" stroke-width="2.2" stroke-linecap="round" stroke-linejoin="round"/></svg>EVENTS</li>
      <li><svg viewBox="0 0 20 20"><circle cx="9" cy="11" r="7.5" fill="none" stroke="var(--red)" stroke-width="1.8"/><path d="M5 10.5 L9 14.5 L18 3" fill="none" stroke="var(--red)" stroke-width="2.2" stroke-linecap="round" stroke-linejoin="round"/></svg>BANQUETS</li>
      <li><svg viewBox="0 0 20 20"><circle cx="9" cy="11" r="7.5" fill="none" stroke="var(--red)" stroke-width="1.8"/><path d="M5 10.5 L9 14.5 L18 3" fill="none" stroke="var(--red)" stroke-width="2.2" stroke-linecap="round" stroke-linejoin="round"/></svg>BINGO</li>
      <li><svg viewBox="0 0 20 20"><circle cx="9" cy="11" r="7.5" fill="none" stroke="var(--red)" stroke-width="1.8"/><path d="M5 10.5 L9 14.5 L18 3" fill="none" stroke="var(--red)" stroke-width="2.2" stroke-linecap="round" stroke-linejoin="round"/></svg>FOOD</li>
    </ul>

    <div class="badge">LINDEN<br>HERITAGE<br>CENTRE</div>

    <div class="call">
      <p class="call-title">CALL US TODAY</p>
      <p class="call-sub">TO GET MORE INFORMATION.</p>
    </div>
    <div class="phone">
      <svg viewBox="0 0 28 28"><circle cx="14" cy="14" r="12.5" fill="none" stroke="var(--white)" stroke-width="1.6"/><path d="M9 7.5 L11.5 7 L13 10.5 L11.3 12 C12 14 13.8 15.8 15.8 16.6 L17.3 15 L20.8 16.4 L20.3 19 C14 19.5 8.5 14 9 7.5 Z" fill="var(--white)"/></svg>
      (604) 555-0172
    </div>
    <div class="footer-divider"></div>
    <ul class="contact">
      <li class="address"><svg viewBox="0 0 18 18"><circle cx="9" cy="9" r="8.2" fill="none" stroke="var(--white)" stroke-width="1.2"/><path d="M9 3.5 C6.6 3.5 5.2 5.2 5.2 7.1 C5.2 9.6 9 14 9 14 C9 14 12.8 9.6 12.8 7.1 C12.8 5.2 11.4 3.5 9 3.5 Z" fill="var(--white)"/><circle cx="9" cy="7.1" r="1.5" fill="var(--navy)"/></svg><span>1480 LINDEN AVENUE<br>VANCOUVER, B.C V5L 2K9</span></li>
      <li class="line"><svg viewBox="0 0 18 18"><circle cx="9" cy="9" r="8.2" fill="none" stroke="var(--white)" stroke-width="1.2"/><rect x="4.5" y="5.8" width="9" height="6.4" fill="none" stroke="var(--white)" stroke-width="1.1"/><path d="M4.5 5.8 L9 9.6 L13.5 5.8" fill="none" stroke="var(--white)" stroke-width="1.1"/></svg>INFO@LINDENHERITAGE.COM</li>
      <li class="line"><svg viewBox="0 0 18 18"><circle cx="9" cy="9" r="8.2" fill="none" stroke="var(--white)" stroke-width="1.2"/><circle cx="9" cy="9" r="5" fill="none" stroke="var(--white)" stroke-width="1"/><ellipse cx="9" cy="9" rx="2.2" ry="5" fill="none" stroke="var(--white)" stroke-width="1"/><path d="M4 9 H14" stroke="var(--white)" stroke-width="1"/></svg>WWW.LINDENHERITAGE.COM</li>
    </ul>
  </div>
</body>
</html>
```